Business Cards and Company profile

I already have a company logo and website, I really need someone to come up with designs that are inkeeping with the theme of the website and the logo.
I need business cards and the company profile reworked (I areadly have the text) as described above.

thanks
Gareth
harbourwaveroutes.example

Target Market(s)

Mainly be for travel trade facing.

Industry/Entity Type

Business

```html
<!DOCTYPE html>
<html lang="en">
<head>
<meta charset="utf-8">
<title>Company Profile – Harbour Wave Routes</title>
<link rel="stylesheet" href="https://fonts.googleapis.com/css2?family=Arimo:wght@400;700&display=swap">
<style>
  :root {
    --brand-yellow: #e0d100;
    --page-white: #ffffff;
    --ink: #1c1c1c;
    --ink-soft: #8a8a8a;
    --backdrop: #2e3033;
  }
  * { margin: 0; padding: 0; box-sizing: border-box; }
  html, body {
    width: 1200px; height: 849px; overflow: hidden;
    background: var(--backdrop);
    font-family: "Arimo", Arial, sans-serif;
    color: var(--ink);
  }
  .canvas { position: relative; width: 1200px; height: 849px; }
  .page {
    position: absolute; top: 72px; width: 503px; height: 712px;
    background: var(--page-white);
    overflow: hidden;
  }
  .page--cover { left: 75px; }
  .page--profile { left: 621px; width: 499px; }

  /* Cover */
  .cover-band {
    position: absolute; left: 0; top: 0; width: 100%; height: 220px;
    background: var(--brand-yellow);
  }
  .cover-title {
    position: absolute; left: 53px; top: 180px;
    font-size: 23px; font-weight: 700; color: var(--page-white);
    letter-spacing: -0.2px; white-space: nowrap;
  }
  .brand-name {
    position: absolute; display: flex; align-items: center; gap: 10px;
    font-weight: 700; color: var(--ink); white-space: nowrap;
  }
  .brand-name__dot {
    display: block; border-radius: 50%; background: var(--brand-yellow);
  }
  .cover-brand { left: 0; width: 100%; justify-content: center; top: 380px; font-size: 26px; letter-spacing: 0.5px; }
  .cover-brand .brand-name__dot { width: 22px; height: 22px; }
  .cover-contact {
    position: absolute; left: 53px; top: 611px;
    font-size: 10px; line-height: 12.5px; white-space: nowrap;
  }
  .cover-contact__label { font-weight: 700; margin-bottom: 12px; }

  /* Profile page */
  .profile-spine {
    position: absolute; left: 0; top: 0; width: 51px; height: 100%;
    background: var(--brand-yellow);
  }
  .profile-brand { left: 51px; right: 0; justify-content: center; top: 92px; font-size: 13px; gap: 6px; letter-spacing: 0.3px; }
  .profile-brand .brand-name__dot { width: 11px; height: 11px; }
  .profile-list {
    position: absolute; left: 116px; top: 0; list-style: none;
    font-size: 8px; line-height: 10px; color: var(--ink);
  }
  .profile-list__item { position: absolute; left: 0; white-space: nowrap; }
  .profile-list__marker { position: absolute; left: 0; }
  .profile-list__text { position: absolute; left: 31px; }
  .profile-section {
    position: absolute; left: 86px; top: 171px; width: 380px;
    font-size: 8px; line-height: 10px; white-space: nowrap;
  }
  .profile-section .profile-list__text { left: 30px; }
  .profile-footer {
    position: absolute; left: 87px; top: 673px;
    font-size: 8.5px; color: var(--ink-soft); white-space: nowrap;
  }
</style>
</head>
<body>
<main class="canvas">

  <section class="page page--cover" aria-label="Cover page">
    <div class="cover-band"></div>
    <h1 class="cover-title">Company Profile of</h1>
    <div class="brand-name cover-brand">
      <span class="brand-name__dot"></span>
      <span>HARBOUR WAVE ROUTES</span>
    </div>
    <div class="cover-contact">
      <p class="cover-contact__label">Main company contact:</p>
      <p>Gareth Ellery – Managing Director</p>
      <p>Email: gareth@harbourwaveroutes.example</p>
      <p>Tel:&nbsp; 01632 960 010</p>
    </div>
  </section>

  <section class="page page--profile" aria-label="Business information page">
    <div class="profile-spine"></div>
    <div class="brand-name profile-brand">
      <span class="brand-name__dot"></span>
      <span>HARBOUR WAVE ROUTES</span>
    </div>

    <div class="profile-section">
      <span class="profile-list__marker">1.</span>
      <span class="profile-list__text">Business, Administrative &amp; Contact Information</span>
    </div>

    <ol class="profile-list">
      <li class="profile-list__item" style="top:202px;"><span class="profile-list__marker">a.</span><span class="profile-list__text">Business name: Harbour Wave Routes</span></li>
      <li class="profile-list__item" style="top:232px;"><span class="profile-list__marker">b.</span><span class="profile-list__text">Business type: Limited</span></li>
      <li class="profile-list__item" style="top:263px;"><span class="profile-list__marker">c.</span><span class="profile-list__text">Company registration number: 1234567</span></li>
      <li class="profile-list__item" style="top:293px;"><span class="profile-list__marker">d.</span><span class="profile-list__text">VAT number: Application in Process</span></li>
      <li class="profile-list__item" style="top:314px;"><span class="profile-list__marker">e.</span><span class="profile-list__text">Trade Associations: Guild of Travel Trade Agents –<br>Application in progress</span></li>
      <li class="profile-list__item" style="top:354px;"><span class="profile-list__marker">f.</span><span class="profile-list__text">Tel: 01632 960 010</span></li>
      <li class="profile-list__item" style="top:385px;"><span class="profile-list__marker">g.</span><span class="profile-list__text">Fax: 01632 960 019</span></li>
      <li class="profile-list__item" style="top:405px;"><span class="profile-list__marker">h.</span><span class="profile-list__text">Website: www.harbourwaveroutes.example</span></li>
      <li class="profile-list__item" style="top:435px;"><span class="profile-list__marker">i.</span><span class="profile-list__text">E-mail: admin@harbourwaveroutes.example</span></li>
      <li class="profile-list__item" style="top:466px;"><span class="profile-list__marker">j.</span><span class="profile-list__text">Emergency Mobile:&nbsp; 07700 900097</span></li>
      <li class="profile-list__item" style="top:497px;"><span class="profile-list__marker">k.</span><span class="profile-list__text">Postal Address: Suite 4, 1st Floor, Marlow House,<br>12 Quayside Road, Essex, ZZ1 1ZZ</span></li>
    </ol>

    <p class="profile-footer">Business Profile of Harbour Wave Routes</p>
  </section>

</main>
</body>
</html>
```